Personal Business Card design contest for freelance work

Include

Proflink.example/in/DanielMWhitacre (as URL and/or QR Code)
Daniel Whitacre
(555) 014-2938
DanielMWhitacre@Mailnest.example
Maplewood, TX

Industry/Entity Type

Business

```html
<!DOCTYPE html>
<html lang="en">
<head>
<meta charset="utf-8">
<title>Daniel Whitacre – Business Card</title>
<link rel="stylesheet" href="https://fonts.googleapis.com/css2?family=Open+Sans:wght@400;600;700;800&display=swap">
<style>
  :root {
    --bg: #e4e4e2;
    --card: #ffffff;
    --blue: #1893d1;
    --navy: #17324f;
    --orange: #f2a71b;
    --orange-deep: #e0582a;
    --green: #4cb848;
    --green-deep: #2f8f3a;
    --ink: #1c2b3a;
    --skin: #e9b99a;
    --suit: #2a2d33;
  }
  * { box-sizing: border-box; margin: 0; padding: 0; }
  html, body { width: 1200px; height: 873px; overflow: hidden; }
  body {
    background: var(--bg);
    font-family: "Open Sans", Arial, sans-serif;
    display: flex;
    align-items: center;
    justify-content: center;
    gap: 40px;
  }
  .card {
    position: relative;
    width: 540px;
    height: 309px;
    background: var(--card);
    box-shadow: 0 2px 6px rgba(0,0,0,.18);
    overflow: hidden;
  }
  .card svg.shapes { position: absolute; inset: 0; }
  .portrait {
    position: absolute;
    border-radius: 10px;
    background: linear-gradient(160deg, var(--skin) 0%, var(--skin) 35%, var(--suit) 36%, var(--suit) 100%);
  }
  .front .portrait { left: 22px; top: 20px; width: 190px; height: 150px; }
  .back .portrait { left: 18px; top: 18px; width: 118px; height: 92px; }
  .name {
    position: absolute;
    color: #fff;
    font-weight: 700;
    text-transform: uppercase;
    line-height: .95;
  }
  .name .first, .name .last { display: block; }
  .front .name { left: 262px; top: 96px; }
  .front .name .first { font-size: 58px; letter-spacing: 2px; }
  .front .name .last { font-size: 38px; letter-spacing: 2px; }
  .back .name { left: 172px; top: 36px; }
  .back .name .first { font-size: 30px; letter-spacing: 1px; }
  .back .name .last { font-size: 21px; letter-spacing: 1px; }
  .profile-link {
    position: absolute;
    left: 24px;
    bottom: 22px;
    font-size: 16px;
    font-weight: 700;
    color: var(--ink);
  }
  .contact-row {
    position: absolute;
    right: 0;
    height: 36px;
    display: flex;
    align-items: center;
  }
  .contact-row .icon {
    width: 36px; height: 36px;
    display: flex; align-items: center; justify-content: center;
    margin-right: 6px;
  }
  .contact-row .bar {
    height: 100%;
    flex: 1;
    display: flex;
    align-items: center;
    padding-left: 12px;
    color: #fff;
    font-size: 16px;
    font-weight: 600;
    letter-spacing: .3px;
    white-space: nowrap;
  }
  .row-phone { top: 138px; left: 208px; }
  .row-phone .icon { background: var(--navy); }
  .row-phone .bar { background: var(--blue); }
  .row-email { top: 182px; left: 168px; }
  .row-email .icon { background: var(--orange-deep); }
  .row-email .bar { background: var(--orange); }
  .row-place { top: 226px; left: 128px; }
  .row-place .icon { background: var(--green-deep); }
  .row-place .bar { background: var(--green); }
</style>
</head>
<body>

<section class="card front">
  <svg class="shapes" width="540" height="309" viewBox="0 0 540 309">
    <path d="M238 92 Q300 40 400 56 Q330 58 270 96 Z" fill="var(--navy)"/>
    <rect x="236" y="70" width="284" height="150" rx="30" fill="var(--blue)"/>
    <path d="M262 212 L214 246 L292 218 Z" fill="var(--blue)"/>
    <path d="M214 246 L262 212 L250 224 Z" fill="var(--navy)"/>
  </svg>
  <div class="portrait" role="img" aria-label="Caricature illustration of Daniel Whitacre in a dark suit holding a tablet"></div>
  <h1 class="name"><span class="first">Daniel</span><span class="last">Whitacre</span></h1>
  <p class="profile-link">Proflink.example/in/DanielMWhitacre</p>
</section>

<section class="card back">
  <svg class="shapes" width="540" height="309" viewBox="0 0 540 309">
    <path d="M156 40 Q190 12 250 18 Q200 22 168 46 Z" fill="var(--orange-deep)"/>
    <rect x="154" y="26" width="178" height="86" rx="18" fill="var(--orange)"/>
    <path d="M168 106 L140 126 L186 110 Z" fill="var(--orange)"/>
  </svg>
  <div class="portrait" role="img" aria-label="Small caricature illustration of Daniel Whitacre in a dark suit"></div>
  <h2 class="name"><span class="first">Daniel</span><span class="last">Whitacre</span></h2>

  <div class="contact-row row-phone">
    <span class="icon">
      <svg width="20" height="20" viewBox="0 0 24 24" aria-hidden="true"><path fill="#fff" d="M6.6 10.8a15.1 15.1 0 0 0 6.6 6.6l2.2-2.2c.3-.3.7-.4 1-.2 1.1.4 2.3.6 3.6.6.6 0 1 .4 1 1V20c0 .6-.4 1-1 1A17 17 0 0 1 3 4c0-.6.4-1 1-1h3.5c.6 0 1 .4 1 1 0 1.3.2 2.5.6 3.6.1.3 0 .7-.2 1z"/></svg>
    </span>
    <span class="bar">(555) 014-2938</span>
  </div>
  <div class="contact-row row-email">
    <span class="icon">
      <svg width="20" height="16" viewBox="0 0 20 16" aria-hidden="true"><rect x="1" y="1" width="18" height="14" fill="none" stroke="#fff" stroke-width="2"/><path d="M1 1 L10 9 L19 1" fill="none" stroke="#fff" stroke-width="2"/></svg>
    </span>
    <span class="bar">DanielMWhitacre@Mailnest.example</span>
  </div>
  <div class="contact-row row-place">
    <span class="icon">
      <svg width="20" height="20" viewBox="0 0 20 20" aria-hidden="true"><path fill="#fff" d="M10 2 L19 10 H16 V18 H12 V13 H8 V18 H4 V10 H1 Z"/></svg>
    </span>
    <span class="bar">Maplewood, TX</span>
  </div>
</section>

</body>
</html>
```